Redesign Website for Corvane Blaze

I have an existing website on https://www.corvaneblaze-demo.com.au/ and would like to have this redesigned professionally with new content (please refer to word document). We are fire protection engineers providing fire services design expertise and engineering design to a range of different clients.

We also provide drafting services to clients in the form of completing final commissioning documentation such as 'as-installed' drawings and fire services block plans to ensure compliance with the building code and relevant Australian Standards.

Target Market(s)

Builders, Architects, Consultants, Project Managers

Industry/Entity Type

Engineering Consultant

Coding

Coded - Design and coding required

Number of Pages Required

4 page

Font styles to use
Sans Serif

Requirements
Must have
• Home and about Page, fire services design page, fire block plans page, contact us page (4 Pages).

The website colour choice must match or compliment the new company logo.
Nice to have
• Quality photos of fire services installations in buildings to Australian Standards.

A website similar to this would be ideal http://quorbelflame-demo.com.au
Should not have
• Stolen licensed photos

```html
<!DOCTYPE html>
<html lang="en">
<head>
<meta charset="utf-8">
<title>Corvane Blaze — Fire Services Design</title>
<link href="https://fonts.googleapis.com/css2?family=Outfit:wght@300;400;500;600;700&display=swap" rel="stylesheet">
<style>
:root{
  --orange:#f7941d;
  --orange-soft:#fde8cf;
  --ink:#111111;
  --body:#333333;
  --muted:#8a8a8a;
  --pale:#f8f7f5;
  --navy:#0f0c27;
  --white:#ffffff;
}
*{margin:0;padding:0;box-sizing:border-box}
html,body{width:1200px;height:5091px;overflow:hidden}
body{font-family:"Outfit",sans-serif;color:var(--body);background:var(--white);position:relative}
.abs{position:absolute}
.btn{position:absolute;background:var(--orange);color:var(--white);font-weight:600;font-size:12px;border-radius:8px;display:flex;align-items:center;justify-content:center;box-shadow:0 10px 22px rgba(247,148,29,.28)}
.eyebrow{color:var(--orange);font-weight:600;font-size:19px}
h2.section-title{position:absolute;font-size:29px;font-weight:600;color:var(--ink);text-align:center;left:0;width:1200px}
.lead{position:absolute;font-size:14px;line-height:23px;color:var(--body);text-align:center}

/* nav */
.brand{position:absolute;display:flex;align-items:center;gap:8px;font-weight:600;font-size:15px;color:var(--orange);letter-spacing:.5px}
.brand-dot{width:14px;height:14px;border-radius:50%;background:var(--orange)}
.nav{position:absolute;top:45px;left:393px;display:flex;gap:30px;font-size:13px;color:var(--ink)}
.nav span:nth-child(1){margin-right:16px}

/* hero */
.hero-art{position:absolute;left:465px;top:150px;width:605px;height:405px}
.hero-sky{position:absolute;left:195px;top:0;width:410px;height:405px;border-radius:60% 40% 25% 50% / 55% 50% 15% 45%;background:linear-gradient(160deg,#8ff0ef 0%,#c9f5e4 50%,#ffe1bd 80%,#fbc27a 100%)}
.hero-flame{position:absolute;left:0;top:215px;width:260px;height:190px;border-radius:70% 50% 20% 40% / 80% 60% 20% 20%;background:linear-gradient(150deg,#fbb03b,#f7941d 60%,#f08a12)}
.hero-title{position:absolute;left:186px;top:190px;font-size:42px;line-height:52px;color:var(--ink);z-index:2}
.hero-title span{display:block;white-space:nowrap}
.hero-title .light{font-weight:400}
.hero-title .bold{font-weight:700}
.scroll{position:absolute;left:188px;top:480px;display:flex;align-items:center;gap:12px;font-size:11px;color:var(--body)}
.scroll i{width:26px;height:26px;border-radius:50%;border:1px solid #ddd;display:flex;align-items:center;justify-content:center}

/* services */
.service{position:absolute;width:200px;text-align:center;font-size:13.5px;font-weight:500;color:var(--ink);line-height:22px}
.icon-badge{width:58px;height:58px;border-radius:50%;background:var(--white);box-shadow:0 8px 20px rgba(0,0,0,.06);margin:0 auto 22px;display:flex;align-items:center;justify-content:center}

/* plans */
.plan{position:absolute;width:230px}
.plan .icon-badge{margin:0 0 26px 0;width:70px;height:70px}
.plan h3{font-size:17px;font-weight:600;color:var(--ink);margin-bottom:18px}
.plan p{font-size:13.5px;line-height:22px;color:var(--body)}

/* testimonials */
.card{position:absolute;top:3248px;width:262px;height:334px;background:var(--white);box-shadow:0 10px 30px rgba(0,0,0,.05);padding:40px 32px}
.stars{color:var(--orange);font-size:14px;letter-spacing:1px;margin-bottom:14px}
.card p{font-size:14px;line-height:22.5px;color:var(--body)}
.person{position:absolute;left:32px;bottom:40px;display:flex;align-items:center;gap:14px}
.avatar{width:38px;height:38px;border-radius:50%;background:linear-gradient(135deg,#a58c7a,#4a3b33)}
.person b{display:block;font-size:14px;color:var(--ink);font-weight:600}
.person small{font-size:10px;color:var(--muted)}
.dots{position:absolute;top:3628px;left:566px;display:flex;gap:18px;align-items:center}
.dots i{width:5px;height:5px;border-radius:50%;background:#bbb}
.dots i.on{width:10px;height:10px;background:var(--orange);box-shadow:0 0 0 4px var(--orange-soft)}

/* contact */
.contact-head{position:absolute;left:188px;top:3780px;font-size:36px;font-weight:700;color:var(--ink)}
.contact-lead{position:absolute;left:188px;top:3850px;width:360px;font-size:14px;line-height:22px}
.c-label{position:absolute;left:188px;font-size:20px;font-weight:500;color:#c9c9c9}
.c-line{position:absolute;left:188px;display:flex;gap:18px;font-size:14px;color:var(--ink);align-items:flex-start;line-height:22px;width:340px}
.form-wrap{position:absolute;left:614px;top:3760px;width:430px;height:624px;border-radius:40px;background:var(--pale)}
.form{position:absolute;left:629px;top:3776px;width:403px;height:593px;background:var(--white);border-radius:30px;box-shadow:0 10px 30px rgba(0,0,0,.04)}
.field{position:absolute;left:40px;width:305px;border-bottom:1px solid #e2e2e2;padding-bottom:10px}
.field label{display:block;font-size:11px;font-weight:600;color:var(--ink);margin-bottom:10px}
.field span{font-size:14px;color:#b7b7b7}

/* footer */
.footer{position:absolute;left:0;top:4389px;width:1200px;height:702px;background:var(--navy);color:var(--white)}
.footer .news{position:absolute;left:188px;top:76px;font-size:29px;font-weight:600;line-height:40px}
.sub{position:absolute;left:613px;top:83px;width:407px;height:71px;border-radius:36px;background:var(--white)}
.sub span{position:absolute;left:44px;top:26px;font-size:13px;color:#777}
.sub b{position:absolute;right:8px;top:14px;width:106px;height:44px;border-radius:22px;background:var(--orange);color:var(--white);font-size:13px;font-weight:600;display:flex;align-items:center;justify-content:center}
.rule{position:absolute;height:1px;background:rgba(255,255,255,.16)}
.fcol{position:absolute;top:286px}
.fcol h4{font-size:17px;font-weight:600;margin-bottom:28px}
.fcol a{display:block;font-size:11px;color:#d8d8e0;margin-bottom:26px;text-decoration:none}
.f-about{position:absolute;left:188px;top:419px;width:230px;font-size:11px;line-height:20px;color:#d8d8e0}
.socials{position:absolute;left:190px;top:491px;display:flex;gap:20px}
.socials i{width:12px;height:12px;border-radius:50%;background:var(--white)}
.copy{position:absolute;top:597px;left:0;width:1200px;text-align:center;font-size:11px;color:#d8d8e0}
</style>
</head>
<body>

<!-- header -->
<div class="brand" style="left:188px;top:44px"><span class="brand-dot"></span>CORVANE BLAZE</div>
<nav class="nav"><span>Home</span><span>About us</span><span>Fire services plans</span><span>Fire block Plans</span><span>Contact us</span></nav>
<div class="btn" style="left:927px;top:35px;width:84px;height:36px;font-size:13px">Login</div>

<!-- hero -->
<div class="hero-art" role="img" aria-label="Illustration of two firefighters carrying a ladder and spraying a hose at orange flames, with a fire truck and sky background">
  <div class="hero-sky"></div>
  <div class="hero-flame"></div>
</div>
<div class="eyebrow abs" style="left:188px;top:148px">Safety First</div>
<h1 class="hero-title"><span class="light">Ensure Fire Safety</span><span class="bold">Save Life &amp; Property</span></h1>
<p class="abs" style="left:188px;top:320px;width:310px;font-size:14px;line-height:24px">Lorem ipsum dolor sit amet consectetur adi piscing elit sed do eiusmod.</p>
<div class="btn" style="left:188px;top:396px;width:118px;height:40px;font-size:11px">Get Started</div>
<div class="scroll"><i><svg width="10" height="10" viewBox="0 0 10 10"><path d="M1 3 L5 8 L9 3Z" fill="var(--orange)"/></svg></i>Scroll Down</div>

<!-- about -->
<div class="abs" style="left:138px;top:593px;width:495px;height:494px;border-radius:70px;background:var(--pale)"></div>
<div class="abs" role="img" aria-label="Photo of a fire services technician in blue overalls in a workshop" style="left:188px;top:633px;width:399px;height:365px;background:linear-gradient(135deg,#6f7478,#2f3437 60%,#4b5a70)"></div>
<div class="abs" role="img" aria-label="Photo of red fire extinguishers mounted beside a hose reel cabinet on a wall" style="left:425px;top:771px;width:233px;height:263px;background:linear-gradient(135deg,#e9e6e2,#d2cdc7 55%,#b8362f 56%,#c9433a);border:5px solid var(--white)"></div>
<div class="eyebrow abs" style="left:712px;top:626px;font-size:17px">About us</div>
<h2 class="abs" style="left:712px;top:662px;font-size:30px;line-height:38px;color:var(--ink);font-weight:400">Discover How We<br><b style="font-weight:600">Can Help You</b></h2>
<p class="abs" style="left:712px;top:760px;width:300px;font-size:13.5px;line-height:22.5px">Corvane Blaze is a company based in Sydney, Australia providing the Australian market expertise in the field of fire safety. Our mission is to assist our clients with the preparation of design and specifications of fire services upgrades and final comm issioning documentation to achieve compliance.</p>
<div class="btn" style="left:712px;top:963px;width:118px;height:40px;font-size:11px">Read More</div>

<!-- fire services drawings -->
<div class="abs" style="left:0;top:1111px;width:1200px;height:724px;background:var(--pale)"></div>
<h2 class="section-title" style="top:1173px">Fire Services Drawings</h2>
<p class="lead" style="left:300px;top:1234px;width:600px;font-size:12.5px;line-height:19.5px">Corvane Blaze can assist with the preparation of the design and specification for the upgrade or installation or new fire safety systems to achieve compliance with the National Construction Code (NCC), Council Fire Orders or Fire Engineering Reports</p>
<p class="lead" style="left:300px;top:1313px;width:600px;font-size:12.5px;line-height:19.5px">We have proficient knowledge in the ability to produce design and specifications relating to the below fire safety measures</p>

<div class="service" style="left:183px;top:1391px"><div class="icon-badge"><svg width="26" height="26" viewBox="0 0 26 26" fill="none" stroke="var(--orange)" stroke-width="1.6"><circle cx="13" cy="13" r="9"/><circle cx="13" cy="13" r="3"/></svg></div>Automatic Smoke<br>Detection and Alarm<br>System</div>
<div class="service" style="left:390px;top:1391px"><div class="icon-badge"><svg width="26" height="26" viewBox="0 0 26 26" fill="none" stroke="var(--orange)" stroke-width="1.6"><path d="M7 19 V12 a6 6 0 0 1 12 0 V19Z"/><path d="M5 21 H21"/></svg></div>Emergency Warning and<br>Intercom System (EWIS)</div>
<div class="service" style="left:606px;top:1391px"><div class="icon-badge"><svg width="26" height="26" viewBox="0 0 26 26" fill="none" stroke="var(--orange)" stroke-width="1.6"><circle cx="13" cy="13" r="8"/><path d="M13 5 V13 L19 16"/></svg></div>Occupant Warning System<br>(OWS)</div>
<div class="service" style="left:817px;top:1391px"><div class="icon-badge"><svg width="26" height="26" viewBox="0 0 26 26" fill="none" stroke="var(--orange)" stroke-width="1.6"><rect x="5" y="5" width="16" height="5"/><path d="M8 14 L13 21 L18 14"/></svg></div>Smoke Alarms</div>

<div class="service" style="left:183px;top:1578px"><div class="icon-badge"><svg width="26" height="26" viewBox="0 0 26 26" fill="none" stroke="var(--orange)" stroke-width="1.6"><circle cx="13" cy="13" r="9"/><circle cx="13" cy="13" r="5"/><circle cx="13" cy="13" r="1.5"/></svg></div>Fire Hose Reels</div>
<div class="service" style="left:390px;top:1578px"><div class="icon-badge"><svg width="26" height="26" viewBox="0 0 26 26" fill="none" stroke="var(--orange)" stroke-width="1.6"><rect x="9" y="8" width="8" height="14" rx="2"/><path d="M11 8 V5 H17 L20 7"/></svg></div>Portable Fire Extinguishers</div>
<div class="service" style="left:606px;top:1578px"><div class="icon-badge"><svg width="26" height="26" viewBox="0 0 26 26" fill="none" stroke="var(--orange)" stroke-width="1.6"><path d="M9 22 V11 a4 4 0 0 1 8 0 V22Z"/><path d="M6 15 H20"/></svg></div>Fire Hydrant Systems</div>
<div class="service" style="left:817px;top:1578px"><div class="icon-badge"><svg width="26" height="26" viewBox="0 0 26 26" fill="none" stroke="var(--orange)" stroke-width="1.6"><rect x="5" y="7" width="16" height="12"/><path d="M10 13 H17 M14 10 L17 13 L14 16"/></svg></div>Emergency Lighting<br>and Exit signs</div>

<div class="btn" style="left:540px;top:1730px;width:120px;height:40px;font-size:11px">Get Started</div>

<!-- how we work -->
<h2 class="section-title" style="top:1900px">let's See How We Work</h2>
<p class="lead" style="left:290px;top:1956px;width:620px">Lorem ipsum dolor sit amet consectetur adipiscing elit sed do eiusmod tempor incididunt ut labore et dolore magna aliqua.</p>
<div class="abs" role="img" aria-label="Photo of a ceiling-mounted sprinkler pipe system in a commercial interior" style="left:0;top:2050px;width:297px;height:411px;background:linear-gradient(160deg,#c8d4da,#6f8592 60%,#3c5a66)"></div>
<div class="abs" role="img" aria-label="Photo of a red fire monitor nozzle at an industrial plant" style="left:297px;top:2050px;width:303px;height:411px;background:linear-gradient(170deg,#bfd6ea,#8a8c8a 45%,#b83a32 70%,#3a3431)"></div>
<div class="abs" role="img" aria-label="Photo of two red fire hydrant valves against a wall" style="left:600px;top:2050px;width:300px;height:411px;background:linear-gradient(180deg,#f6a84a,#f08f23);opacity:.92">
  <svg class="abs" style="left:138px;top:194px" width="24" height="24" viewBox="0 0 24 24"><path d="M12 2 V22 M2 12 H22" stroke="#fff" stroke-width="2"/></svg>
</div>
<div class="abs" role="img" aria-label="Photo of red fire sprinkler valve pipework in a plant room" style="left:900px;top:2050px;width:300px;height:411px;background:linear-gradient(150deg,#d9dcde,#b9463c 50%,#8a8f93)"></div>

<!-- fire block plans -->
<h2 class="section-title" style="top:2530px">Fire Block Plans</h2>
<p class="lead" style="left:290px;top:2585px;width:620px">We can also assist you with the preparation of final commissioning documentation as required to achieve with relevant Australian Standards. Some of the services we provide (but not limited to) include</p>
<div class="plan" style="left:208px;top:2683px"><div class="icon-badge"><svg width="30" height="30" viewBox="0 0 30 30" fill="none" stroke="var(--orange)" stroke-width="1.6"><ellipse cx="15" cy="13" rx="10" ry="5"/><path d="M5 13 V17 a10 5 0 0 0 20 0 V13"/></svg></div><h3>Zone Block Plans</h3><p>Lorem ipsum dolor sit amet consectetur adipisicing elit sed. do eiusmod temporin.</p></div>
<div class="plan" style="left:492px;top:2683px"><div class="icon-badge"><svg width="30" height="30" viewBox="0 0 30 30" fill="none" stroke="var(--orange)" stroke-width="1.6"><path d="M6 12 H11 L19 6 V24 L11 18 H6Z"/><path d="M22 11 a5 5 0 0 1 0 8"/></svg></div><h3>EWIS / SSISEP Block Plans</h3><p>Lorem ipsum dolor sit amet consectetur adipisicing elit sed. do eiusmod temporin.</p></div>
<div class="plan" style="left:775px;top:2683px"><div class="icon-badge"><svg width="30" height="30" viewBox="0 0 30 30" fill="none" stroke="var(--orange)" stroke-width="1.6"><path d="M8 7 H22 M15 7 V14 M10 14 H20 L15 22Z"/></svg></div><h3>Sprinkler Block Plans</h3><p>Lorem ipsum dolor sit amet consectetur adipisicing elit sed. do eiusmod temporin.</p></div>
<div class="btn" style="left:540px;top:2934px;width:120px;height:40px;font-size:11px">View More</div>

<!-- testimonials -->
<div class="abs" style="left:0;top:3047px;width:1200px;height:666px;background:var(--pale)"></div>
<h2 class="section-title" style="top:3108px">What People Say</h2>
<p class="lead" style="left:320px;top:3164px;width:560px">Lorem ipsum dolor sit amet consectetur adipisicing elit sed do eiusmod tempor incididunt ut labore et dolore.</p>
<div class="card" style="left:188px"><div class="stars">★★★★☆</div><p>sed do eiusmod tempor incididunt ut labore et dolore magna aliqua. Ut enim ad minim veniam, quis nostrud exercitation ullamco laboris nisi ut aliquip ex eammodo consequatDuis aute.</p><div class="person"><span class="avatar" role="img" aria-label="Reviewer portrait"></span><div><b>John Doe</b><small>Happy People</small></div></div></div>
<div class="card" style="left:469px"><div class="stars">★★★★☆</div><p>sed do eiusmod tempor incididunt ut labore et dolore magna aliqua. Ut enim ad minim veniam, quis nostrud exercitation ullamco laboris nisi ut aliquip ex eammodo consequat Dui.</p><div class="person"><span class="avatar" role="img" aria-label="Reviewer portrait"></span><div><b>John Doe</b><small>Happy People</small></div></div></div>
<div class="card" style="left:751px"><div class="stars">★★★★☆</div><p>sed do eiusmod tempor incididunt ut labore et dolore magna aliqua. Ut enim ad minim veniam, quis nostrud exercitation ullamco laboris nisi ut aliquip ex eammodo consequat Duis.</p><div class="person"><span class="avatar" role="img" aria-label="Reviewer portrait"></span><div><b>John Doe</b><small>Happy People</small></div></div></div>
<div class="dots"><i class="on"></i><i></i><i></i><i></i></div>

<!-- contact -->
<h2 class="contact-head">Get In Touch</h2>
<p class="contact-lead">consectetur adipisicing elit, sed do eiusmod tempor incididunt ut labore et dolore magna aliqua. Ut en-im.ad</p>
<div class="c-label" style="top:3940px">Location</div>
<div class="c-line" style="top:3988px"><svg width="14" height="18" viewBox="0 0 14 18"><path d="M7 0 a6 6 0 0 1 6 6 c0 5 -6 12 -6 12 s-6 -7 -6 -12 a6 6 0 0 1 6 -6Z" fill="var(--ink)"/><circle cx="7" cy="6" r="2.2" fill="#fff"/></svg><span>Lorem ipsum dolor sit amet, consectetur. adipisicing elit,</span></div>
<div class="c-label" style="top:4060px">Need Help?</div>
<div class="c-line" style="top:4112px"><svg width="16" height="12" viewBox="0 0 16 12"><rect width="16" height="12" fill="var(--ink)"/><path d="M0 0 L8 7 L16 0" stroke="#fff" fill="none"/></svg><span style="font-size:13px">info@corvaneblaze-demo.com.au</span></div>
<div class="c-label" style="top:4158px">Feel like Talking</div>
<div class="c-line" style="top:4208px"><svg width="14" height="14" viewBox="0 0 14 14"><path d="M2 0 L5 0 L6 4 L4 5 C5 8 6 9 9 10 L10 8 L14 9 L14 12 C14 13 13 14 12 14 C6 14 0 8 0 2 C0 1 1 0 2 0Z" fill="var(--ink)"/></svg><span style="font-size:13px">+614 55 019 274</span></div>

<div class="form-wrap"></div>
<div class="form">
  <div class="field" style="top:50px"><label>Your name</label><span>John Doe</span></div>
  <div class="field" style="top:132px"><label>Contact E-mail</label><span>you@example.com</span></div>
  <div class="field" style="top:213px"><label>Phone Number</label><span>+987 654 321</span></div>
  <div class="field" style="top:294px"><label>Phone Number</label><span>+987 654 321</span></div>
  <div class="field" style="top:377px;border:none"><label>Your message</label><span>Write your message</span></div>
  <div class="btn" style="left:40px;top:480px;width:305px;height:52px;font-size:14px">Send Message</div>
</div>

<!-- footer -->
<footer class="footer">
  <div class="news">Get update by signup<br>Newsletter.</div>
  <div class="sub"><span>Enter your email</span><b>Join</b></div>
  <div class="rule" style="left:188px;top:219px;width:824px"></div>
  <div class="brand" style="left:188px;top:318px"><span class="brand-dot"></span>CORVANE BLAZE</div>
  <p class="f-about">Lorem ipsum dolor sit amet, consectetur adipiscing elit, sed do eiusmod tempor incididunt ut labore et dolore.</p>
  <div class="socials"><i></i><i></i><i></i><i></i></div>
  <div class="fcol" style="left:613px"><h4>Company</h4><a>Home</a><a>About Us</a><a>Fire services plans</a><a>Fire block Plans</a><a>Contact us</a></div>
  <div class="fcol" style="left:765px"><h4>Support</h4><a>Terms &amp; Policy</a><a>Privacy</a><a>Legal</a></div>
  <div class="fcol" style="left:917px"><h4>Socials</h4><a>Friendwall</a><a>Chirper</a><a>Snapgrid</a><a>Shotboard</a></div>
  <div class="rule" style="left:170px;top:559px;width:866px"></div>
  <div class="copy">Copyrights © 2021 Corvane Blaze. All Right Reserved</div>
</footer>

</body>
</html>
```